Letterhead design for business

Looking for an attractive and professional letterhead that uses the logo that is attached below.

Target Market(s)

Potential bankruptcy clients.

Industry/Entity Type

Legal

Colors

Designer to choose colors to be used in the design.

Requirements
Must have
• Address for locations, phone number, and website address.
• Addresses are on website ferncoveadvice.example. Use following phone number (for tracking purposes): 555-013-8274

```html
<!DOCTYPE html>
<html lang="en">
<head>
<meta charset="utf-8">
<title>Ferncove Advice Letterhead</title>
<link href="https://fonts.googleapis.com/css2?family=Open+Sans:wght@400;600&family=Arimo:wght@400;700&display=swap" rel="stylesheet">
<style>
  :root {
    --paper: #ffffff;
    --ink: #3a3a3a;
    --ink-soft: #4a4a4a;
    --green: #72bd7e;
    --charcoal: #2f2f31;
  }
  html, body {
    margin: 0;
    padding: 0;
    width: 1040px;
    height: 1200px;
    overflow: hidden;
    background: var(--paper);
  }
  .letterhead {
    position: relative;
    width: 1040px;
    height: 1200px;
    background: var(--paper);
    font-family: "Open Sans", Arial, sans-serif;
    color: var(--ink);
  }
  .brand {
    position: absolute;
    left: 97px;
    top: 88px;
    display: flex;
    align-items: center;
    gap: 14px;
  }
  .brand-dot {
    width: 30px;
    height: 30px;
    border-radius: 50%;
    background: var(--green);
  }
  .brand-name {
    font-family: "Open Sans", Arial, sans-serif;
    font-weight: 600;
    font-size: 36px;
    color: var(--ink);
    letter-spacing: -0.5px;
  }
  .offices {
    position: absolute;
    left: 583px;
    top: 44px;
    font-family: "Arimo", Arial, sans-serif;
    font-size: 17px;
    line-height: 21px;
    color: var(--ink);
  }
  .offices p { margin: 0 0 9px; }
  .phone { margin-top: 12px; }
  .phone-label { color: var(--green); font-weight: 700; }
  .letter {
    position: absolute;
    left: 97px;
    width: 841px;
    font-size: 15px;
    color: var(--ink-soft);
  }
  .issue-date { top: 297px; }
  .recipient { top: 332px; line-height: 19px; }
  .salutation { top: 438px; }
  .body-copy { top: 488px; line-height: 27.5px; text-align: justify; hyphens: auto; }
  .body-copy p { margin: 0 0 26px; }
  .closing { top: 895px; }
  .signature-mark {
    position: absolute;
    left: 97px;
    top: 932px;
    width: 240px;
    height: 26px;
    background: linear-gradient(90deg, #e6e6e6, #f3f3f3);
  }
  .signatory { top: 970px; }
  .signatory-name { font-size: 18px; font-weight: 600; color: var(--ink); margin: 0 0 6px; }
  .signatory-role { margin: 0; }
  .footer-band-green {
    position: absolute;
    left: 84px;
    top: 1143px;
    width: 472px;
    height: 9px;
    background: var(--green);
  }
  .footer-band-dark {
    position: absolute;
    left: 84px;
    top: 1161px;
    width: 659px;
    height: 6px;
    background: var(--charcoal);
  }
  .website {
    position: absolute;
    left: 770px;
    top: 1152px;
    font-family: "Arimo", Arial, sans-serif;
    font-size: 17px;
    color: var(--ink);
  }
  .website .accent { color: var(--green); }
</style>
</head>
<body>
<div class="letterhead">
  <header>
    <div class="brand">
      <span class="brand-dot"></span>
      <span class="brand-name">Ferncove Advice</span>
    </div>
    <div class="offices">
      <p>418 Larkmoor Ave.,<br>Suite #1400 Brookhaven Ridge 30910</p>
      <p>2215 Oakridge Rd. Millbrook<br>Falls 30822</p>
      <p class="phone"><span class="phone-label">T:</span> 555-013-8274</p>
    </div>
  </header>

  <div class="letter issue-date">Issuing Date: May 5, 2018</div>
  <div class="letter recipient">Name Of Employee Mr. XYZABC<br>Address of Employee<br>Address Line 2 etc..</div>
  <div class="letter salutation">Dear Mr.XYZABC</div>

  <div class="letter body-copy" lang="en">
    <p>Lorem Ipsum has been the industry's standard dummy text ever since the 1500s, when an unknown printer took a galley of type and scrambled it to make a type specimen book. It has survived not only five centuries, but also the leap into electronic typesetting, remaining essentially unchanged. It was popularised in the 1960s with the release of Vellmark sheets containing Lorem Ipsum passages, and more recently with desktop publishing software like Quillset Layout including versions of Lorem Ipsum.</p>
    <p>Lorem Ipsum is simply dummy text of the printing and typesetting industry. Lorem Ipsum has been the industry's standard dummy text ever since the 1500s, when an unknown printer took a galley of type and scrambled it to make a type specimen book.</p>
    <p>It has survived not only five centuries, but also the leap into electronic typesetting, remaining essentially unchanged. It was popularised in the 1960s with the release of Vellmark sheets containing Lorem IpsumIpsum passages.</p>
  </div>

  <div class="letter closing">Yours Sincerely</div>
  <div class="signature-mark" role="img" aria-label="Handwritten signature of Marcus Ellery"></div>
  <div class="letter signatory">
    <p class="signatory-name">Marcus Ellery</p>
    <p class="signatory-role">Managing Director</p>
  </div>

  <footer>
    <div class="footer-band-green"></div>
    <div class="footer-band-dark"></div>
    <div class="website">www.<span class="accent">ferncoveadvice</span>.example</div>
  </footer>
</div>
</body>
</html>
```